loft 17 design

We are needing a website built for our company. We are based in the Dallas/Ft. Worth area providing staging for realtors, occupied staging, apartments, builders and hospitality industry ( Roam Pods .) Have been in the design and furniture industry for 35+ years, looking to expand our services to the area. Here Are some of the buzzword used for staging. Turn properties into dream spaces. Staging preparing property for sale.
Design services offered for new construction . We want to incorporate our tag line Turning you property into a dream Space .
interior and home design
Coded - Design and coding required
2 page

```html
<!DOCTYPE html>
<html lang="en">
<head>
<meta charset="utf-8">
<title>Loft 17 Design — Home Staging</title>
<link href="https://fonts.googleapis.com/css2?family=Lora:wght@500;600;700&family=Lato:wght@400;700&display=swap" rel="stylesheet">
<style>
:root{
  --blue:#1b4ea3;
  --blue-deep:#123b80;
  --ink:#1b1b1b;
  --muted:#6b6b6b;
  --dark:#262626;
  --light:#e3e3e3;
  --white:#ffffff;
}
*{box-sizing:border-box;margin:0;padding:0}
html,body{width:1200px;height:4552px;overflow:hidden}
body{font-family:"Lato",Arial,sans-serif;color:var(--ink);background:var(--white);position:relative}
section,header,footer{position:absolute;left:0;width:1200px}

/* header + hero */
.site-header{top:0;height:80px;z-index:3}
.brand{position:absolute;left:120px;top:8px;font-family:"Lora",Georgia,serif;font-weight:700;font-size:30px;letter-spacing:2px;color:var(--ink)}
.brand small{display:block;font-family:"Lato",sans-serif;font-size:9px;letter-spacing:3px;font-weight:700}
.main-nav{position:absolute;left:352px;top:25px;display:flex;gap:22px;font-size:14px;white-space:nowrap}
.main-nav a{color:var(--ink);text-decoration:none}
.call-btn{position:absolute;left:912px;top:16px;width:148px;height:38px;background:var(--blue);color:#fff;font-size:15px;font-weight:700;border-radius:3px;display:flex;align-items:center;justify-content:center;gap:8px;white-space:nowrap}
.hero{top:0;height:680px;background:linear-gradient(90deg,#f7f7f7,#fff 60%)}
.hero-sketch{position:absolute;left:40px;top:70px;width:560px;height:540px;background:radial-gradient(ellipse at 45% 50%,#eceff1 0%,rgba(247,247,247,0) 70%)}
.hero h1{position:absolute;left:130px;top:180px;width:480px;font-family:"Lora",Georgia,serif;font-weight:700;font-size:44px;line-height:1.2;color:var(--blue)}
.hero p{position:absolute;left:130px;top:318px;width:440px;font-size:13px;line-height:1.55;color:#444}
.btn-outline{position:absolute;left:130px;top:398px;width:180px;height:40px;border:2px solid var(--blue);color:var(--blue);font-size:15px;display:flex;align-items:center;justify-content:center}
.hero-photo{position:absolute;left:608px;top:112px;width:480px;height:512px;border-radius:60px 0 60px 0;background:linear-gradient(135deg,#eef0f2,#c9ccd1 55%,#8f8578)}

.section-title{position:absolute;font-family:"Lora",Georgia,serif;font-weight:700;font-size:34px;color:var(--blue);display:flex;align-items:center;gap:14px;white-space:nowrap}
.section-title::before{content:"";width:46px;height:3px;background:currentColor}
.section-sub{position:absolute;font-size:13px;color:var(--muted)}

/* partners */
.partners{top:700px;height:400px}
.partner-row{position:absolute;left:120px;top:220px;width:960px;display:flex;justify-content:space-between}
.partner{width:160px;height:100px;background:#fff;box-shadow:0 2px 14px rgba(0,0,0,.07);display:flex;align-items:center;justify-content:center;gap:8px;font-weight:700;font-size:19px;color:#3a3a5a}
.partner i{width:10px;height:10px;border-radius:50%;background:#3a3a5a;display:block}

/* services */
.services{top:1100px;height:460px}
.service-row{position:absolute;left:160px;top:150px;width:880px;display:flex;justify-content:space-between}
.service{width:190px;text-align:center}
.service svg{width:34px;height:34px;fill:var(--blue)}
.service h3{font-family:"Lora",Georgia,serif;font-size:20px;color:var(--blue);margin:8px 0 10px;white-space:nowrap}
.service p{font-size:12px;line-height:1.45;color:#333}

/* projects */
.projects{top:1560px;height:1220px;background:var(--dark)}
.projects .section-title{color:#fff;left:0;width:1200px;justify-content:center;top:70px}
.tabs{position:absolute;top:140px;left:0;width:1200px;display:flex;justify-content:center;gap:22px;font-size:15px;color:#ddd}
.tabs span{padding:6px 12px}
.tabs .on{background:var(--blue);color:#fff;border-radius:3px}
.grid{position:absolute;top:220px;left:0;width:1200px;height:800px;display:grid;grid-template-columns:repeat(3,400px);grid-template-rows:400px 400px}
.tile{position:relative}
.t1{background:linear-gradient(160deg,#5b6268,#2d2f31)}
.t2{background:linear-gradient(160deg,#8b5a44,#3c2a24)}
.t3{background:linear-gradient(160deg,#d8d2c8,#6e5a48)}
.t4{background:linear-gradient(160deg,#e6e6e6,#7a7a7a)}
.t5{background:linear-gradient(160deg,#6f7a55,#3b3a2e)}
.t6{background:linear-gradient(160deg,#f0eeea,#9a9188)}
.overlay{position:absolute;inset:0;background:rgba(0,0,0,.45)}
.overlay h4{position:absolute;left:30px;top:150px;font-family:"Lora",Georgia,serif;font-size:32px;color:#fff;font-weight:500}
.overlay span{position:absolute;left:30px;top:212px;border:1px solid #fff;color:#fff;font-size:14px;padding:8px 26px}
.dots{position:absolute;top:1095px;left:0;width:1200px;display:flex;justify-content:center;gap:14px}
.dots i{width:16px;height:16px;border-radius:50%;border:2px solid #fff;display:block}
.dots i:first-child{background:#fff}

/* testimonials */
.testimonials{top:2780px;height:640px;background:var(--light)}
.testimonials .section-title{left:0;width:1200px;justify-content:center;top:70px;font-size:30px}
.testimonials .section-sub{left:0;width:1200px;text-align:center;top:128px}
.cards{position:absolute;top:200px;left:120px;width:960px;display:flex;justify-content:space-between}
.card{width:290px;height:310px;background:#fff;text-align:center;padding:30px 28px}
.avatar{width:80px;height:80px;border-radius:50%;margin:0 auto 26px;background:linear-gradient(135deg,#666,#222)}
.card p{font-size:12px;line-height:1.5;color:#555;margin-bottom:26px}
.card b{font-size:12px;font-weight:400;color:#555}
.arrow{position:absolute;top:330px;width:60px;height:30px}

/* contact */
.contact{top:3420px;height:800px;background:linear-gradient(100deg,#3a3a3a 0%,#1c1c1c 45%,#4b4b4b 75%,#2a2a2a 100%)}
.contact .section-title{color:#fff;left:128px;top:70px;font-size:30px}
.contact .section-sub{left:128px;top:124px;width:440px;color:#fff;font-size:13px;line-height:1.5}
.form{position:absolute;left:128px;top:200px;width:412px;height:500px;background:rgba(30,30,30,.85);padding:24px 20px}
.field{background:#fff;height:54px;margin-bottom:20px;padding:16px 14px;font-size:13px;color:#777}
.field.tall{height:170px}
.send{background:var(--blue);color:#fff;font-size:14px;width:190px;height:42px;display:flex;align-items:center;justify-content:center}

/* footer */
.site-footer{top:4220px;height:332px;background:#fff}
.footer-brand{position:absolute;left:128px;top:30px;font-family:"Lora",Georgia,serif;font-weight:700;font-size:46px;line-height:1;letter-spacing:3px}
.footer-brand small{display:block;font-family:"Lato",sans-serif;font-size:10px;letter-spacing:4px}
.fcol{position:absolute;top:40px;width:180px;font-size:12px;line-height:1.8;color:var(--blue)}
.fcol h5{font-family:"Lora",Georgia,serif;font-size:13px;color:var(--ink);margin-bottom:8px;letter-spacing:1px;white-space:nowrap}
.fcol h5::before{content:"— "}
.social{display:flex;gap:10px;margin-top:10px}
.social i{width:14px;height:14px;border-radius:50%;background:var(--blue);display:block}
.copyright{position:absolute;left:0;bottom:0;width:1200px;height:52px;background:var(--blue-deep);color:#fff;font-size:11px;display:flex;align-items:center;justify-content:center}
</style>
</head>
<body>

<header class="site-header">
  <div class="brand">LOFT 17<small>DESIGN STUDIO</small></div>
  <nav class="main-nav"><a>Home</a><a>Real Estate</a><a>Interior Design</a><a>Portfolio</a><a>About Us</a><a>Blog</a><a>Contact</a></nav>
  <div class="call-btn"><svg width="14" height="14" viewBox="0 0 24 24" fill="#fff"><path d="M6.6 10.8a15 15 0 006.6 6.6l2.2-2.2a1 1 0 011-.25 11.4 11.4 0 003.6.6 1 1 0 011 1V20a1 1 0 01-1 1A17 17 0 013 4a1 1 0 011-1h3.5a1 1 0 011 1 11.4 11.4 0 00.6 3.6 1 1 0 01-.25 1z"/></svg>555 014 2290</div>
</header>

<section class="hero">
  <div class="hero-sketch" role="img" aria-label="Faint line sketch of a room interior"></div>
  <h1>Turning You Property Into A Dream Space</h1>
  <p>Over 35+ Years Of Experience In Turning Every Room Into A Space Buyers Remember. We Stage The Properties That Help Sellers Move Faster For Their Clients.</p>
  <div class="btn-outline">Learn More</div>
  <div class="hero-photo" role="img" aria-label="Bright staged living room with sofa and tall windows"></div>
</section>

<section class="partners">
  <h2 class="section-title" style="left:100px;top:50px">Our Partners</h2>
  <p class="section-sub" style="left:120px;top:118px">Several Partners Who Have Worked With Us To Create Dream Projects</p>
  <div class="partner-row">
    <div class="partner"><i></i>brightly</div>
    <div class="partner">PLANEO</div>
    <div class="partner">Hollen</div>
    <div class="partner">Marlo</div>
    <div class="partner">tidewell</div>
  </div>
</section>

<section class="services">
  <h2 class="section-title" style="left:100px;top:30px">Redesign Realty</h2>
  <div class="service-row">
    <div class="service"><svg viewBox="0 0 24 24"><circle cx="12" cy="12" r="10"/><text x="12" y="16.5" font-size="12" text-anchor="middle" fill="#fff" font-family="Lato">$</text></svg><h3>Sell Your House</h3><p>Lorem ipsum dolor sit amet consectetur. Ac nunc interdum scelerisque id eu tincidunt nulla porta quis. Etiam imperdiet nec sed quis morbi dui.</p></div>
    <div class="service"><svg viewBox="0 0 24 24"><path d="M12 3L2 12h3v9h5v-6h4v6h5v-9h3z"/></svg><h3>Buy a Home</h3><p>Lorem ipsum dolor sit amet consectetur. Ac nunc interdum scelerisque id eu tincidunt nulla porta quis. Etiam imperdiet nec sed quis morbi dui.</p></div>
    <div class="service"><svg viewBox="0 0 24 24"><path d="M3 4h18v12H3zM8 20h8v-2H8z"/></svg><h3>Upgrade Your Home</h3><p>Lorem ipsum dolor sit amet consectetur. Ac nunc interdum scelerisque id eu tincidunt nulla porta quis. Etiam imperdiet nec sed quis morbi dui.</p></div>
    <div class="service"><svg viewBox="0 0 24 24"><circle cx="8" cy="8" r="4"/><circle cx="17" cy="9" r="3"/><path d="M1 20c0-4 3-6 7-6s7 2 7 6zM14 20c0-2 0-4-1-5 4-1 10 0 10 5z"/></svg><h3>Agent Partnership</h3><p>Lorem ipsum dolor sit amet consectetur. Ac nunc interdum scelerisque id eu tincidunt nulla porta quis. Etiam imperdiet nec sed quis morbi dui.</p></div>
  </div>
</section>

<section class="projects">
  <h2 class="section-title">Our Projects</h2>
  <div class="tabs"><span class="on">Show All</span><span>Bathroom</span><span>Bedroom</span><span>Kitchen</span><span>Living Room</span></div>
  <div class="grid">
    <div class="tile t1" role="img" aria-label="Living room with leather sofa and fireplace"><div class="overlay"><h4>Villa in the forest</h4><span>Show Detail</span></div></div>
    <div class="tile t2" role="img" aria-label="Bedroom with patterned bedding and warm lamps"></div>
    <div class="tile t3" role="img" aria-label="Seating area with armchairs by a window"></div>
    <div class="tile t4" role="img" aria-label="Open plan living space with stone fireplace"></div>
    <div class="tile t5" role="img" aria-label="Balcony with hanging chair and plants"></div>
    <div class="tile t6" role="img" aria-label="Lounge with grey sofa and round tables"></div>
  </div>
  <div class="dots"><i></i><i></i><i></i><i></i><i></i></div>
</section>

<section class="testimonials">
  <h2 class="section-title">What Clients Say?</h2>
  <p class="section-sub">Below Are Some Testimonials From Our Clients</p>
  <svg class="arrow" style="left:40px" viewBox="0 0 60 30" fill="none" stroke="#222" stroke-width="3"><path d="M58 15H4M16 3L4 15l12 12"/></svg>
  <div class="cards">
    <div class="card"><div class="avatar" role="img" aria-label="Client portrait"></div><p>Pellentesque risus netus condimentum consectetur mollis quis purus. Pellentesque adipiscing a nunc vulputate tincidunt.</p><b>Home Seller - Plano</b></div>
    <div class="card"><div class="avatar" role="img" aria-label="Client portrait"></div><p>Pellentesque risus netus condimentum consectetur mollis quis purus. Pellentesque adipiscing a nunc vulputate tincidunt.</p><b>Realtor - Fort Worth</b></div>
    <div class="card"><div class="avatar" role="img" aria-label="Client portrait"></div><p>Pellentesque risus netus condimentum consectetur mollis quis purus. Pellentesque adipiscing a nunc vulputate tincidunt.</p><b>Builder - Frisco</b></div>
  </div>
  <svg class="arrow" style="right:40px" viewBox="0 0 60 30" fill="none" stroke="#222" stroke-width="3"><path d="M2 15h54M44 3l12 12-12 12"/></svg>
</section>

<section class="contact" role="img" aria-label="Dark interior photo of a person working at a laptop">
  <h2 class="section-title">Get in Touch!</h2>
  <p class="section-sub">Ready To Redesign Your Real Estate? Let's Start Talking About Your Project Today. Our Team Will Help You Stage Your Home Into A Dream Space.</p>
  <div class="form">
    <div class="field">Name*</div>
    <div class="field">Email*</div>
    <div class="field">Phone Number*</div>
    <div class="field tall">Your Message*</div>
    <div class="send">Send Message</div>
  </div>
</section>

<footer class="site-footer">
  <div class="footer-brand">LOFT<br>17<small>DESIGN STUDIO</small></div>
  <div class="fcol" style="left:348px"><h5>ABOUT US</h5>Lorem sed interdum nisl, nisi aliquam in nulla a tincidunt. Curabitur mauris netus pretium.<div class="social"><i></i><i></i><i></i></div></div>
  <div class="fcol" style="left:568px"><h5>OTHER LINKS</h5>Register<br>Sign In<br>Affiliate<br>FAQ</div>
  <div class="fcol" style="left:738px"><h5>RELATED LINKS</h5>About Us<br>Why Buy With Us?<br>Our Partners<br>Contact Us</div>
  <div class="fcol" style="left:918px"><h5>REACH US</h5>Terms<br>Licenses<br>Become an affiliate<br>Help Center</div>
  <div class="copyright">© 2024 LOFT 17 DESIGN. ALL RIGHTS RESERVED</div>
</footer>

</body>
</html>
```